Company Values Poster

Project Brief: Refinement of Brantow Core Values Visuals
Overview
Brantow Power Controls Pty Ltd is seeking a designer to refine and improve the visual presentation of our company core values, ensuring they are clear, modern, scalable, and aligned with our existing brand identity.

We are not looking for a complete rebrand. The objective is to elevate and sharpen our current values artwork so it works consistently across
internal presentations and onboarding material, signage, decals, and digital assets.

Scope of Work
The designer will be required to:
- Refine and modernise our existing core values icons and layout
- Improve visual consistency, spacing, hierarchy, and legibility
- Ensure icons and typography scale cleanly for both digital and print
- Maintain strong alignment with our current branding, colours, fonts, and tone
- Provide a polished, professional, engineering-led aesthetic
- Core Values (Content to Remain Conceptually Consistent)

The following values already exist and should remain conceptually intact, but may be visually refined:

Always Evolving
Stay curious, adapt, and share to grow.

Straight Talk
Be real. No triangles, no bullshit.

Respect Builds Trust
Value people and put them first.

Do It Once, Do It Right
Put your name on it.

Safety First, Own It
We prioritise the safety of our people and our customers.

One Team
One standard, no passengers.

Brand Alignment (Critical)
- Designs must align strictly with our existing brand guidelines and visual language.
We will provide:
- Current core values design (requires resolution and layout improvement)
- Brantow brand specifications (colours, fonts, logo usage)
- Brantow-Brand-Specifications
- Primary Brantow logo
- Brantow logo mark

Key brand attributes:
- Engineering-led
- Practical, no-nonsense
- Quality, safety, and trust focused
- Industrial / infrastructure context (not consumer or tech-startup style)
- Style Direction
- Clean, modern, and confident
- Strong iconography with clear meaning
- Avoid gimmicks, gradients, or over-complex illustration
- Must feel appropriate for critical electrical infrastructure, heavy industry, and energy projects
- Consistent line weights and icon geometry preferred
Deliverables
- Refined core values layout (full set)
- Individual icon files for each value
- High-resolution assets suitable for: Web, Print, Presentations, Editable source files

```html
<!DOCTYPE html>
<html lang="en">
<head>
<meta charset="utf-8">
<title>Brantow Core Values</title>
<link href="https://fonts.googleapis.com/css2?family=Baloo+2:wght@500;800&family=Montserrat:wght@800&display=swap" rel="stylesheet">
<style>
  :root {
    --frame-grey: #bebfc1;
    --paper: #ffffff;
    --brand-green: #065228;
    --brand-red: #e83137;
    --ink: #000000;
    --icon-tint-a: #e4efe8;
    --icon-tint-b: #f6dcdd;
  }
  * { margin: 0; padding: 0; box-sizing: border-box; }
  html, body { width: 1200px; height: 770px; overflow: hidden; }
  body { background: var(--frame-grey); font-family: "Baloo 2", sans-serif; }

  .poster {
    position: relative;
    width: 1200px;
    height: 770px;
    background: var(--frame-grey);
  }
  .poster-sheet {
    position: absolute;
    left: 82px; top: 74px;
    width: 1035px; height: 628px;
    background: var(--paper);
    overflow: hidden;
  }

  .brand-name {
    position: absolute;
    left: 0; right: 0; top: 56px;
    display: flex; align-items: center; justify-content: center; gap: 10px;
    font-family: "Montserrat", sans-serif;
    font-weight: 800;
    font-size: 50px;
    letter-spacing: 1px;
    color: var(--brand-green);
    line-height: 1;
  }
  .brand-dot {
    width: 14px; height: 14px; border-radius: 50%;
    background: var(--brand-red);
  }

  .values-row {
    position: absolute;
    left: 56px; top: 166px;
    display: flex; gap: 15.5px;
  }
  .value-card {
    width: 141px; height: 194px;
    border: 4px solid var(--brand-green);
    border-radius: 16px;
    display: flex; flex-direction: column; align-items: center;
    padding-top: 9px;
    text-align: center;
  }
  .value-icon {
    width: 100px; height: 100px;
    border-radius: 14px;
    background: radial-gradient(circle at 50% 45%, var(--icon-tint-b) 0%, var(--icon-tint-a) 70%);
  }
  .value-title {
    margin-top: 9px;
    font-weight: 800;
    font-size: 17px;
    line-height: 14.5px;
    text-transform: uppercase;
    color: var(--brand-green);
    letter-spacing: 0.2px;
  }
  .value-text {
    margin-top: 2px;
    font-weight: 500;
    font-size: 11px;
    line-height: 11.5px;
    color: var(--ink);
  }

  .title-band {
    position: absolute;
    left: 282px; top: 402px;
    width: 753px; height: 94px;
    background: var(--brand-green);
    display: flex; align-items: center;
    padding-left: 150px;
  }
  .title-band h1 {
    font-family: "Montserrat", sans-serif;
    font-weight: 800;
    font-size: 70px;
    line-height: 1;
    color: var(--paper);
    letter-spacing: 0.5px;
  }

  .ribbon {
    position: absolute;
    left: 0; top: 0;
    width: 1035px; height: 628px;
    pointer-events: none;
  }
  .ribbon-red { fill: var(--brand-red); }
  .ribbon-black { fill: var(--ink); }
</style>
</head>
<body>
<main class="poster">
  <section class="poster-sheet">
    <header class="brand-name">Brantow<span class="brand-dot"></span></header>

    <div class="values-row">
      <article class="value-card">
        <div class="value-icon" role="img" aria-label="Icon: gears turning inside circular arrows"></div>
        <h2 class="value-title">Always<br>Evolving</h2>
        <p class="value-text">Stay Curious, adapt<br>and share to grow</p>
      </article>
      <article class="value-card">
        <div class="value-icon" role="img" aria-label="Icon: two speech bubbles in conversation"></div>
        <h2 class="value-title">Straight<br>Talk</h2>
        <p class="value-text">Be Real. No Triangles<br>No Bullshit</p>
      </article>
      <article class="value-card">
        <div class="value-icon" role="img" aria-label="Icon: open hand holding a hard hat"></div>
        <h2 class="value-title">Respect<br>Builds Trust</h2>
        <p class="value-text">Value people and<br>put them first</p>
      </article>
      <article class="value-card">
        <div class="value-icon" role="img" aria-label="Icon: tick inside a gear ring"></div>
        <h2 class="value-title">Do It Once,<br>Do It Right</h2>
        <p class="value-text">Put your name on it</p>
      </article>
      <article class="value-card">
        <div class="value-icon" role="img" aria-label="Icon: shield with a tick and gear"></div>
        <h2 class="value-title">Safety First,<br>Own It</h2>
        <p class="value-text">We prioritise the safety<br>of our people and<br>our customers</p>
      </article>
      <article class="value-card">
        <div class="value-icon" role="img" aria-label="Icon: group of team members standing together"></div>
        <h2 class="value-title">One<br>Team</h2>
        <p class="value-text">One Standard<br>No passengers</p>
      </article>
    </div>

    <svg class="ribbon" viewBox="0 0 1035 628" aria-hidden="true">
      <polygon class="ribbon-red" points="63,474 275,474 275,504 718,569 63,569 107,522"/>
      <polygon class="ribbon-black" points="332,504 769,504 769,569"/>
    </svg>

    <div class="title-band">
      <h1>CORE VALUES</h1>
    </div>
  </section>
</main>
</body>
</html>
```